Business Card Design

We have our logo and everything in place. Looking to have a layout for our new business cards designed. These will be printed with a matte finish, possibly rounded corners, and looking to incorporate some cool spot UV layers into the design.

Ive uploaded the existing card front and back as well as our logo.

Card Size Will Be 3.5" x 2"

Industry/Entity Type

Business

```html
<!DOCTYPE html>
<html lang="en">
<head>
<meta charset="utf-8">
<title>Timberline Deck and Rail – Business Cards</title>
<link rel="stylesheet" href="https://fonts.googleapis.com/css2?family=Didact+Gothic&display=swap">
<style>
  :root {
    --bg: #d9d4cc;
    --card: #0c0c0d;
    --card-edge: #1c1c1e;
    --sheen: #2a2a2d;
    --white: #f4f4f4;
    --grey: #b9bcc0;
    --silver: #9ea2a8;
    --blue: #3f9be0;
    --rule: #8d8f93;
  }
  * { box-sizing: border-box; margin: 0; padding: 0; }
  html, body { width: 1200px; height: 781px; overflow: hidden; }
  body {
    background: var(--bg);
    font-family: "Didact Gothic", "Century Gothic", sans-serif;
    display: flex;
    align-items: center;
    justify-content: center;
    gap: 40px;
  }
  .card {
    position: relative;
    width: 540px;
    height: 309px;
    border-radius: 26px;
    background: var(--card);
    overflow: hidden;
    box-shadow: 0 10px 24px rgba(0,0,0,.28);
    color: var(--white);
  }
  .card-front .texture {
    position: absolute; inset: 0;
    background: radial-gradient(ellipse at 55% 35%, #3a3a3c 0%, #161617 45%, var(--card) 80%);
  }
  .brand {
    position: absolute;
    display: flex;
    flex-direction: column;
    align-items: flex-start;
  }
  .brand-name {
    display: flex; align-items: center; gap: 12px;
    font-size: 44px; letter-spacing: 1px; color: var(--white);
  }
  .brand-mark { width: 14px; height: 14px; background: var(--white); }
  .brand-tag {
    margin-top: 6px;
    font-size: 12px; letter-spacing: 4px; text-transform: uppercase; color: var(--white);
    border-top: 1px solid var(--rule); padding-top: 6px; width: 100%;
  }
  .card-front .brand { left: 72px; top: 112px; }
  .card-back .sheen {
    position: absolute; inset: 0;
    background: linear-gradient(115deg, transparent 46%, var(--sheen) 50%, transparent 54%),
                linear-gradient(180deg, #151517 0%, var(--card) 70%);
  }
  .card-back .brand { left: 26px; top: 130px; }
  .card-back .brand-name { font-size: 28px; color: var(--silver); gap: 8px; }
  .card-back .brand-mark { width: 10px; height: 10px; background: var(--silver); }
  .card-back .brand-tag { font-size: 9px; letter-spacing: 3px; color: var(--silver); }
  .contact {
    position: absolute; left: 278px; top: 34px; right: 20px;
  }
  .person-name { font-size: 22px; letter-spacing: 1.5px; text-transform: uppercase; }
  .person-name .first { color: var(--blue); }
  .person-role {
    font-size: 15px; color: var(--grey);
    border-bottom: 1px solid var(--rule); padding-bottom: 8px; margin-bottom: 18px;
    width: 210px;
  }
  .line { font-size: 15px; margin-bottom: 14px; white-space: nowrap; }
  .line .accent { color: var(--blue); }
  .phone { font-size: 18px; letter-spacing: 1px; }
  .service-area {
    position: absolute; left: 20px; right: 20px; bottom: 22px;
    text-align: right; font-size: 17px; letter-spacing: .5px; color: var(--white);
  }
</style>
</head>
<body>
  <section class="card card-front" aria-label="Card front">
    <div class="texture" role="img" aria-label="Dark brushed wood-grain texture"></div>
    <div class="brand">
      <div class="brand-name"><span class="brand-mark"></span>Timberline</div>
      <div class="brand-tag">Deck and Rail</div>
    </div>
  </section>

  <section class="card card-back" aria-label="Card back">
    <div class="sheen"></div>
    <div class="brand">
      <div class="brand-name"><span class="brand-mark"></span>Timberline</div>
      <div class="brand-tag">Deck and Rail</div>
    </div>
    <div class="contact">
      <div class="person-name"><span class="first">Marcus</span>Ellery</div>
      <div class="person-role">president</div>
      <div class="line phone">403.555.0187</div>
      <div class="line"><span class="accent">timberline</span>deckrail@mailbox.com</div>
      <div class="line"><span class="accent">timberline</span>deckrail.com</div>
    </div>
    <div class="service-area">Serving Calgary and surrounding areas</div>
  </section>
</body>
</html>
```